Marlow & Tate
Business card and stationery design for a management consulting firm  - Consulting
Simple
Benedikt Owen Dolsquin
Lead Consultant
Njegoševa 47 11000 Belgrade
benedikt.owen@marlowtate-example.com
www.marlowtate-example.com
Keep the design clean. "Scandinavian design approach". Address line on business card is preferred not to be included, although if designer finds it to complete the holistic 'picture' of the card, then he/she may use it. Font selection for the rest of the text is up to the designer. Although please note that the font has to be in balance with the logo. Business cards are to be printed on black paper / metal. If printed on paper, the logo part will be with relief printing.
This is designers choice to be creative
dolsquin dolsquin
Tip to designers: Try not to use the monogram "MT" with "Marlow and Tate" on the same side. Printing techniques that will be used are: Embossing / Debossing, Thermography. Keep it clean. Less is more.

```html
<!DOCTYPE html>
<html lang="en">
<head>
<meta charset="utf-8">
<title>Marlow &amp; Tate — Business Card</title>
<link rel="stylesheet" href="https://fonts.googleapis.com/css2?family=Crimson+Text:wght@400&display=swap">
<style>
  :root {
    --backdrop-top: #9a9a9a;
    --backdrop-bottom: #6e6e6e;
    --card-black: #0d0d0d;
    --swoosh-grey: #a9a7a8;
    --swoosh-white: #f4f4f4;
    --ink-light: #e8e8e8;
    --ink-muted: #bdbdbd;
  }
  * { box-sizing: border-box; margin: 0; padding: 0; }
  html, body { width: 1200px; height: 984px; overflow: hidden; }
  body {
    background: linear-gradient(180deg, var(--backdrop-top), var(--backdrop-bottom));
    font-family: "Crimson Text", "Times New Roman", serif;
    position: relative;
  }
  .card {
    position: absolute;
    left: 215px;
    width: 770px;
    height: 440px;
    background: var(--card-black);
    border-radius: 26px;
    overflow: hidden;
    box-shadow: 0 14px 30px rgba(0,0,0,0.35);
  }
  .card--front { top: 36px; }
  .card--back { top: 508px; }
  .card__swoosh { position: absolute; inset: 0; width: 100%; height: 100%; }
  .wordmark {
    position: absolute;
    color: var(--ink-light);
    font-size: 46px;
    letter-spacing: 1px;
    white-space: nowrap;
    display: flex;
    align-items: center;
    gap: 14px;
  }
  .wordmark__dot {
    width: 10px; height: 10px; border-radius: 50%;
    background: var(--ink-light);
  }
  .card--front .wordmark { left: 175px; top: 150px; }
  .card--back .wordmark { left: 250px; top: 70px; font-size: 40px; }
  .contact {
    position: absolute;
    right: 78px;
    top: 200px;
    text-align: right;
    color: var(--ink-light);
    font-size: 19px;
    line-height: 1.35;
  }
  .contact__name { font-size: 25px; }
  .contact__role { color: var(--ink-muted); font-size: 18px; margin-bottom: 16px; }
  .contact__icons {
    position: absolute;
    right: 40px;
    bottom: 58px;
    display: flex;
    flex-direction: column;
    gap: 16px;
  }
  .contact__icons svg { width: 18px; height: 18px; display: block; }
</style>
</head>
<body>
  <section class="card card--front" aria-label="Card front">
    <svg class="card__swoosh" viewBox="0 0 770 440" aria-hidden="true">
      <path fill="var(--swoosh-grey)" d="M770,118 C690,138 675,258 598,330 C555,372 515,420 462,440 L770,440 Z"/>
      <path fill="var(--swoosh-white)" d="M770,152 C705,170 700,282 632,348 C592,388 562,424 522,440 L770,440 Z"/>
    </svg>
    <div class="wordmark"><span class="wordmark__dot"></span>Marlow and Tate</div>
  </section>

  <section class="card card--back" aria-label="Card back">
    <svg class="card__swoosh" viewBox="0 0 770 440" aria-hidden="true">
      <path fill="var(--swoosh-grey)" d="M0,92 C95,100 112,205 165,300 C205,378 250,424 300,440 L0,440 Z"/>
      <path fill="var(--swoosh-white)" d="M0,122 C80,132 96,225 142,312 C176,378 214,422 256,440 L232,440 C190,420 152,380 120,318 C80,240 66,150 0,146 Z"/>
      <path fill="var(--swoosh-grey)" d="M0,146 C66,150 80,240 120,318 C152,380 190,420 232,440 L0,440 Z"/>
    </svg>
    <div class="wordmark"><span class="wordmark__dot"></span>Marlow and Tate</div>
    <div class="contact">
      <p class="contact__name">Benedikt Owen Dolsquin</p>
      <p class="contact__role">Lead Consultant</p>
      <p>Njegoševa 47</p>
      <p>11000 Belgrade</p>
      <p>381 60 5 247 036</p>
      <p>benedikt.owen@marlowtate-example.com</p>
      <p>www.marlowtate-example.com</p>
    </div>
    <div class="contact__icons" aria-hidden="true">
      <svg viewBox="0 0 20 20"><path fill="var(--ink-light)" d="M5 2 L8 6 L6.5 8 C7.5 10 9.5 12 12 13.5 L14 12 L18 15 L16 18 C9 17.5 2.5 11 2 4 Z"/></svg>
      <svg viewBox="0 0 20 20"><rect x="2" y="5" width="16" height="11" rx="1" fill="none" stroke="var(--ink-light)" stroke-width="1.6"/><path d="M2.5 5.5 L10 11 L17.5 5.5" fill="none" stroke="var(--ink-light)" stroke-width="1.6"/></svg>
      <svg viewBox="0 0 20 20"><circle cx="10" cy="10" r="8" fill="none" stroke="var(--ink-light)" stroke-width="1.6"/><path d="M2 10 H18 M10 2 C6 6 6 14 10 18 M10 2 C14 6 14 14 10 18" fill="none" stroke="var(--ink-light)" stroke-width="1.3"/></svg>
    </div>
  </section>
</body>
</html>
```